ecommerce website design for pool store

I need a homepage designed for an e-commerce store for a pool shop. It will be similar to https://www.wavecrestaqua.com.au/ but not an exact copy (ie. the icons, photos and colour scheme need to be different). wavecrestaqua.com.au is one of our competitors but we love everything about their website.
I have attached the logo for this site. We want the background to be white and the colours used on the site to be the blue from the logo and the blue and green used on www.bramblenest.com.au
I want the same layout for the logo, search and menu bar at the top along with the 'shop filter cartidges' feature button
Under that a similar slideshow
Under that, the categories with the logos, the best sellers, trending now (but call this 'latest products') and all the other same elements as on this example site.

```html
<!DOCTYPE html>
<html lang="en">
<head>
<meta charset="utf-8">
<title>Clearwave Pool Store</title>
<link href="https://fonts.googleapis.com/css2?family=Roboto:wght@400;500;700&family=Roboto+Condensed:wght@700&display=swap" rel="stylesheet">
<style>
:root{
  --navy:#2e3a8f;
  --sky:#29aae1;
  --ink:#1d1d1d;
  --band:#dce9f1;
  --line:#c9c9c9;
  --white:#ffffff;
}
*{box-sizing:border-box;margin:0;padding:0}
html,body{width:1200px;height:2853px;overflow:hidden;background:var(--white);font-family:'Roboto',sans-serif;color:var(--ink)}
.page{position:relative;width:1200px;height:2853px}
.abs{position:absolute}
.topbar{left:0;top:0;width:1200px;height:32px;background:var(--navy);color:var(--white);font-size:12px}
.topbar .offers{position:absolute;left:427px;top:9px;white-space:nowrap}
.topbar .offers span{margin:0 10px}
.topbar .login{position:absolute;left:952px;top:8px;font-size:12px}
.logo{left:150px;top:9px;width:132px;height:132px;border-radius:50%;border:3px solid var(--navy);background:var(--white);box-shadow:0 0 0 5px #fff;display:flex;align-items:center;justify-content:center;text-align:center;z-index:3}
.logo span{font-family:'Roboto Condensed',sans-serif;font-weight:700;color:var(--navy);font-size:14px;line-height:1.2;letter-spacing:1px}
.search{left:424px;top:48px;width:366px;height:43px;border:1px solid var(--line);font-size:12px;padding:14px 20px;color:#444}
.search-btn{left:790px;top:48px;width:44px;height:43px;background:var(--sky);display:flex;align-items:center;justify-content:center}
.btn{background:linear-gradient(90deg,var(--navy),var(--sky));color:var(--white);font-weight:700;font-size:13px;display:flex;align-items:center;justify-content:center}
.filter-btn{left:846px;top:48px;width:209px;height:43px}
.nav{left:0;top:105px;width:1200px;height:47px;background:var(--band)}
.nav ul{list-style:none;position:absolute;left:304px;top:16px;display:flex;gap:38px;font-size:13px;color:#333}
.nav .active{position:relative}
.nav .active:before{content:"";position:absolute;left:-2px;right:-6px;top:-16px;height:3px;background:var(--sky)}
.hero{left:0;top:152px;width:1200px;height:380px;background:linear-gradient(100deg,#4a4f55 0%,#8a9aa5 28%,#2fa0d6 55%,#6fcaf0 100%)}
.hero-badge{left:773px;top:202px;width:280px;height:280px;border-radius:50%;background:var(--white);border:5px solid var(--navy);text-align:center;font-family:'Roboto Condensed',sans-serif}
.hero-badge .t1{margin-top:58px;font-size:42px;color:var(--sky);line-height:1}
.hero-badge .t2{font-size:42px;color:var(--navy);line-height:1.1}
.hero-badge .shop{margin:18px auto 0;width:114px;height:40px;font-family:'Roboto',sans-serif}
.arrows{display:flex;justify-content:center;gap:4px;margin-top:18px}
.arrows i{width:26px;height:26px;border:1px solid #555;border-radius:50%;display:flex;align-items:center;justify-content:center}
.h2{width:1200px;left:0;text-align:center;font-family:'Roboto Condensed',sans-serif;font-weight:700;font-size:40px}
.h2 span{background:linear-gradient(90deg,var(--navy),var(--sky));-webkit-background-clip:text;background-clip:text;color:transparent}
.cat{width:210px;text-align:center}
.cat .ring{width:208px;height:208px;border-radius:50%;border:4px solid var(--navy);border-right-color:var(--sky);border-bottom-color:var(--sky);padding:16px;margin:0 auto}
.cat .photo{width:100%;height:100%;border-radius:50%}
.cat p{margin-top:20px;font-weight:500;font-size:15px}
.card{width:216px}
.card .photo{width:216px;height:225px;border:1px solid var(--line);padding:30px}
.card .photo div{width:100%;height:100%;border-radius:6px}
.card .name{margin-top:26px;font-weight:500;font-size:15px}
.card .price{margin-top:10px;color:var(--sky);font-size:18px;font-weight:500}
.card .add{margin-top:17px;width:122px;height:40px}
.chev{width:20px;height:30px}
.foot-bg{left:0;top:2397px;width:1200px;height:456px;background:var(--navy)}
.brands{left:48px;top:2194px;width:1104px;height:321px;background:var(--white);border-radius:10px;box-shadow:0 2px 10px rgba(0,0,0,.15)}
.brand{width:216px;height:99px;border:1px solid #999;display:flex;align-items:center;justify-content:center;gap:8px;font-size:38px;color:#333}
.brand i{width:30px;height:30px;border-radius:50%;background:#555}
.fh{color:var(--white);font-family:'Roboto Condensed',sans-serif;font-size:19px}
.fl{color:var(--white);font-size:13px;line-height:31px}
.email{left:786px;top:2615px;width:249px;height:36px;background:var(--white);border-radius:3px;font-size:11px;padding:11px 18px}
.subscribe{left:786px;top:2661px;width:249px;height:37px;background:var(--sky);color:var(--white);font-weight:700;font-size:13px;border-radius:3px;display:flex;align-items:center;justify-content:center}
.legal{left:162px;top:2795px;color:var(--white);font-size:12px}
.pay{top:2794px;width:32px;height:21px;background:#e8eef5;border-radius:2px}
.social{top:2794px;width:20px;height:20px;border-radius:50%;background:var(--white)}
</style>
</head>
<body>
<div class="page">

  <div class="abs topbar">
    <div class="offers">Free Shipping Australia Wide<span>|</span>Buy Now, Pay Later, Paysplit<span>|</span>60 Day Easy Returns</div>
    <div class="login">Login / Join</div>
    <svg class="abs" style="left:1030px;top:5px" width="26" height="22" viewBox="0 0 26 22" fill="none" stroke="#fff" stroke-width="1.6"><path d="M1 2h4l3 13h13l3-9H7"/><circle cx="10" cy="19" r="1.6"/><circle cx="19" cy="19" r="1.6"/></svg>
  </div>

  <div class="abs logo"><span>CLEARWAVE<br>POOL STORE</span></div>

  <div class="abs search">Search</div>
  <div class="abs search-btn"><svg width="16" height="16" viewBox="0 0 16 16" fill="none" stroke="#fff" stroke-width="2.2"><circle cx="6.5" cy="6.5" r="5"/><path d="M10 10l5 5"/></svg></div>
  <div class="abs btn filter-btn">SHOP FILTER CARTRIDGES</div>

  <nav class="abs nav"><ul>
    <li class="active">HOME</li><li>ABOUT</li><li>PRODUCTS</li><li>SHOP</li><li>CATEGORIES</li><li>BEST SELLERS</li><li>TRENDING NOW</li><li>CONTACT</li>
  </ul></nav>

  <div class="abs hero" role="img" aria-label="Person lifting a robotic pool cleaner out of a blue swimming pool"></div>
  <div class="abs hero-badge">
    <div class="t1">CLEARWAVE</div>
    <div class="t2">POOL STORE</div>
    <div class="btn shop">SHOP NOW</div>
    <div class="arrows">
      <i><svg width="8" height="12" viewBox="0 0 8 12" fill="none" stroke="#333" stroke-width="1.6"><path d="M6 1L1 6l5 5"/></svg></i>
      <i><svg width="8" height="12" viewBox="0 0 8 12" fill="none" stroke="#333" stroke-width="1.6"><path d="M2 1l5 5-5 5"/></svg></i>
    </div>
  </div>

  <h2 class="abs h2" style="top:598px"><span>CATEGORIES</span></h2>
  <svg class="abs chev" style="left:86px;top:780px;width:24px;height:40px" viewBox="0 0 24 40" fill="none" stroke="#555" stroke-width="4"><path d="M20 2L4 20l16 18"/></svg>
  <svg class="abs chev" style="left:1090px;top:780px;width:24px;height:40px" viewBox="0 0 24 40" fill="none" stroke="#555" stroke-width="4"><path d="M4 2l16 18L4 38"/></svg>
  <div class="abs cat" style="left:147px;top:694px"><div class="ring"><div class="photo" role="img" aria-label="Yellow pool filter cartridge" style="background:radial-gradient(circle,#f2a81d 30%,#f4f4f4 70%)"></div></div><p>FILTER CARTRIDGES</p></div>
  <div class="abs cat" style="left:379px;top:694px"><div class="ring"><div class="photo" role="img" aria-label="Pool cleaner head in clear water" style="background:radial-gradient(circle,#2b55b8 15%,#d7ecf7 55%)"></div></div><p>POOL CLEANERS</p></div>
  <div class="abs cat" style="left:611px;top:694px"><div class="ring"><div class="photo" role="img" aria-label="Blue and black pool pump" style="background:radial-gradient(circle,#1e6fd6 25%,#f5f5f5 60%)"></div></div><p>POOL PUMPS</p></div>
  <div class="abs cat" style="left:842px;top:694px"><div class="ring"><div class="photo" role="img" aria-label="Folded blue striped pool cover" style="background:radial-gradient(circle,#3b63d8 30%,#f5f5f5 62%)"></div></div><p>POOL COVERS</p></div>

  <h2 class="abs h2" style="top:1053px"><span>BEST SELLERS</span></h2>
  <svg class="abs chev" style="left:105px;top:1247px" viewBox="0 0 20 30" fill="none" stroke="#222" stroke-width="3"><path d="M15 3L4 15l11 12"/></svg>
  <svg class="abs chev" style="left:1075px;top:1247px" viewBox="0 0 20 30" fill="none" stroke="#222" stroke-width="3"><path d="M5 3l11 12L5 27"/></svg>
  <div class="abs card" style="left:143px;top:1148px"><div class="photo"><div role="img" aria-label="Yellow and orange foam pool noodles" style="background:linear-gradient(135deg,#fff 20%,#f6e54a 40%,#f28a2e 65%,#fff 80%)"></div></div><div class="name">LIQUIP EX EA COMMO</div><div class="price">$24.78</div><div class="btn add">ADD TO CART</div></div>
  <div class="abs card" style="left:375px;top:1148px"><div class="photo"><div role="img" aria-label="Round blue above-ground pool" style="background:radial-gradient(ellipse,#5f95e4 35%,#fff 70%)"></div></div><div class="name">LIQUIP EX EA COMMO</div><div class="price">$24.78</div><div class="btn add">ADD TO CART</div></div>
  <div class="abs card" style="left:608px;top:1148px"><div class="photo"><div role="img" aria-label="Rectangular blue pool shell" style="background:linear-gradient(160deg,#fff 15%,#4fb8ee 40%,#2a8ad8 70%,#fff 85%)"></div></div><div class="name">LIQUIP EX EA COMMO</div><div class="price">$24.78</div><div class="btn add">ADD TO CART</div></div>
  <div class="abs card" style="left:840px;top:1148px"><div class="photo"><div role="img" aria-label="Yellow foot pump with blue hose" style="background:radial-gradient(circle,#f7d21e 30%,#2a7fd8 55%,#fff 72%)"></div></div><div class="name">LIQUIP EX EA COMMO</div><div class="price">$24.78</div><div class="btn add">ADD TO CART</div></div>

  <h2 class="abs h2" style="top:1638px"><span>LATEST PRODUCTS</span></h2>
  <svg class="abs chev" style="left:105px;top:1831px" viewBox="0 0 20 30" fill="none" stroke="#222" stroke-width="3"><path d="M15 3L4 15l11 12"/></svg>
  <svg class="abs chev" style="left:1075px;top:1831px" viewBox="0 0 20 30" fill="none" stroke="#222" stroke-width="3"><path d="M5 3l11 12L5 27"/></svg>
  <div class="abs card" style="left:143px;top:1732px"><div class="photo"><div role="img" aria-label="Blue pool wall brush" style="background:linear-gradient(160deg,#fff 25%,#3b63c8 45%,#8fb7ee 60%,#fff 78%)"></div></div><div class="name">LIQUIP EX EA COMMO</div><div class="price">$24.78</div><div class="btn add">ADD TO CART</div></div>
  <div class="abs card" style="left:375px;top:1732px"><div class="photo"><div role="img" aria-label="Robotic pool cleaner with teal tracks" style="background:radial-gradient(circle,#1f2b2b 25%,#3bb6a8 48%,#fff 70%)"></div></div><div class="name">LIQUIP EX EA COMMO</div><div class="price">$24.78</div><div class="btn add">ADD TO CART</div></div>
  <div class="abs card" style="left:608px;top:1732px"><div class="photo"><div role="img" aria-label="Light blue pool noodle" style="background:linear-gradient(150deg,#fff 30%,#5ec7ef 50%,#fff 70%)"></div></div><div class="name">LIQUIP EX EA COMMO</div><div class="price">$24.78</div><div class="btn add">ADD TO CART</div></div>
  <div class="abs card" style="left:840px;top:1732px"><div class="photo"><div role="img" aria-label="Pool control panel" style="background:linear-gradient(180deg,#eef0f3,#c9cdd3)"></div></div><div class="name">LIQUIP EX EA COMMO</div><div class="price">$24.78</div><div class="btn add">ADD TO CART</div></div>

  <div class="abs foot-bg"></div>
  <div class="abs brands"></div>
  <h2 class="abs h2" style="top:2254px"><span>BRANDS WE LOVE</span></h2>
  <svg class="abs chev" style="left:105px;top:2382px" viewBox="0 0 20 30" fill="none" stroke="#222" stroke-width="3"><path d="M15 3L4 15l11 12"/></svg>
  <svg class="abs chev" style="left:1075px;top:2382px" viewBox="0 0 20 30" fill="none" stroke="#222" stroke-width="3"><path d="M5 3l11 12L5 27"/></svg>
  <div class="abs brand" style="left:143px;top:2348px"><i></i>orbitra</div>
  <div class="abs brand" style="left:375px;top:2348px"><i></i>lumeno</div>
  <div class="abs brand" style="left:608px;top:2348px"><i></i>fernly</div>
  <div class="abs brand" style="left:840px;top:2348px"><i></i>kestra</div>

  <div class="abs fh" style="left:162px;top:2571px">LINKS</div>
  <div class="abs fl" style="left:162px;top:2603px">Pumps<br>Filters<br>Chlorinators<br>Cleaners</div>
  <div class="abs fl" style="left:275px;top:2603px">Lights<br>Covers<br>Heaters<br>Hoses</div>
  <div class="abs fh" style="left:423px;top:2571px">ABOUT</div>
  <div class="abs fl" style="left:423px;top:2603px">About us<br>Reviews<br>Blog<br>Free Quote</div>
  <div class="abs fh" style="left:596px;top:2571px">SUPPORT</div>
  <div class="abs fl" style="left:596px;top:2603px">Shipping<br>Returns<br>Payment<br>Paysplit</div>
  <div class="abs fh" style="left:786px;top:2571px">JOIN THE EMAIL PARTY!</div>
  <div class="abs email">Enter Email</div>
  <div class="abs subscribe">SUBSCRIBE</div>

  <div class="abs legal">© 2022, Clearwave Pool Store.All Rights Reserved &nbsp;|&nbsp; Terms &amp; Conditions &nbsp;|&nbsp; Privacy Policy</div>
  <div class="abs pay" style="left:711px"></div>
  <div class="abs pay" style="left:751px"></div>
  <div class="abs pay" style="left:791px"></div>
  <div class="abs pay" style="left:831px"></div>
  <div class="abs pay" style="left:871px"></div>
  <div class="abs social" style="left:933px"></div>
  <div class="abs social" style="left:975px"></div>
  <div class="abs social" style="left:1017px"></div>
</div>
</body>
</html>
```